Use Existing Logo to Design Letterhead, Envelope and Presentation Folder

We are a storm shelter company based out of Oklahoma City. We have an existing logo and brand image. We are looking for professionally designed letterhead, mailing envelopes and folders using our brand guidelines (attached). The font to be used is Futura.

The image represents simple professionalism.
We compete on quality, not price.
We value attention to detail and craftsmanship in our work.
The colors and layout are bold and clean.

Again, this is for:
1) Letterhead - contains name, address, phone, fax, and website address
2) Envelopes - logo, tagline and return address
3) Presentation Folders - logo and tag line

Our tag line is:
"America's Best EF5 Rated Storm Shelters and Family Safety Products"

Please submit your designs and once we have the initial layouts, we will provide the top designers with our contact information.

Good luck!

```html
<!DOCTYPE html>
<html lang="en">
<head>
<meta charset="utf-8">
<title>Steadfast Shelters – Stationery Set</title>
<link href="https://fonts.googleapis.com/css2?family=Jost:wght@400;500;700&display=swap" rel="stylesheet">
<style>
  :root {
    --brand-blue: #0d4da1;
    --brand-grey: #939598;
    --ink: #333333;
    --paper: #ffffff;
    --frame: #555555;
    --edge: #000000;
  }
  * { box-sizing: border-box; margin: 0; padding: 0; }
  html, body { width: 900px; height: 1200px; overflow: hidden; background: var(--edge); }
  .board {
    position: relative; width: 900px; height: 1200px; overflow: hidden;
    font-family: "Jost", "Futura", sans-serif; color: var(--ink);
  }
  .sheet-area {
    position: absolute; left: 26px; top: 0; width: 846px; height: 1198px;
    background: var(--paper); border-right: 1px solid #777; border-bottom: 1px solid #777;
  }
  .piece {
    position: absolute; background: var(--paper); border: 1px solid var(--frame); overflow: hidden;
  }
  .band { position: absolute; left: 0; right: 0; bottom: 0; background: var(--brand-blue); }
  .brand-name {
    position: absolute; font-weight: 500; color: var(--brand-blue);
    text-transform: uppercase; white-space: nowrap; line-height: 1;
  }
  .brand-mark { display: inline-block; background: var(--brand-blue); vertical-align: middle; }
  .address-line {
    position: absolute; left: 0; right: 0; text-align: center;
    font-size: 5px; white-space: nowrap; color: var(--ink);
  }
  .address-line b { font-weight: 700; }
  .web-line {
    position: absolute; left: 0; right: 0; text-align: center; font-size: 5px;
  }
  .tagline {
    position: absolute; left: 0; right: 0; text-align: center; white-space: nowrap;
    text-transform: uppercase; font-weight: 700;
  }

  /* letterhead */
  .letterhead { left: 189px; top: 26px; width: 250px; height: 353px; }
  .letterhead .brand-name { right: 6px; top: 22px; font-size: 7px; }
  .letterhead .address-line { top: 328px; }
  .letterhead .band { height: 12px; }
  .letterhead .web-line { bottom: 3px; color: #fff; }

  /* envelope front */
  .envelope-front { left: 466px; top: 23px; width: 249px; height: 123px; }
  .envelope-front .brand-name { right: 4px; top: 14px; font-size: 5.5px; }
  .envelope-front .tagline {
    left: auto; right: 30px; top: 18px; font-size: 2.6px; font-weight: 400; color: var(--brand-grey);
  }
  .envelope-front .band { height: 18px; }

  /* envelope back */
  .envelope-back { left: 467px; top: 181px; width: 249px; height: 170px; border: none; background: transparent; overflow: visible; }
  .envelope-back svg { position: absolute; left: 0; top: 0; }
  .envelope-back .brand-name { left: 0; right: 0; text-align: center; top: 136px; font-size: 6px; }
  .envelope-back .address-line { top: 155px; }

  /* folder cover */
  .folder-cover { left: 188px; top: 425px; width: 250px; height: 352px; }
  .folder-cover .brand-name { left: 0; right: 0; text-align: center; top: 172px; font-size: 21px; letter-spacing: 0.5px; }
  .folder-cover .brand-name .brand-mark { width: 14px; height: 14px; margin-right: 8px; margin-top: -4px; }
  .folder-cover .band { height: 46px; }
  .folder-cover .tagline { bottom: 1px; font-size: 5.2px; color: #fff; letter-spacing: 0.6px; }

  /* folder back */
  .folder-back { left: 447px; top: 425px; width: 250px; height: 352px; }
  .folder-back .brand-name { left: 0; right: 0; text-align: center; top: 290px; font-size: 8px; }
  .folder-back .address-line { top: 327px; }
  .folder-back .web-line { top: 334px; color: var(--brand-blue); }

  /* folder inside */
  .folder-inside-left { left: 186px; top: 831px; width: 249px; height: 352px; }
  .folder-inside-right { left: 449px; top: 831px; width: 249px; height: 352px; }
  .folder-inside-right svg { position: absolute; left: 0; top: 0; }
</style>
</head>
<body>
<main class="board">
  <div class="sheet-area"></div>

  <section class="piece letterhead" aria-label="Letterhead">
    <div class="brand-name">Steadfast Shelters</div>
    <p class="address-line"><b>Address:</b> This is not actual address. This is only dummy text. Phone: XX 123456, XX 1234556, Fax: XX 123456</p>
    <div class="band"></div>
    <p class="web-line">www.steadfast-example.com</p>
  </section>

  <section class="piece envelope-front" aria-label="Envelope front">
    <p class="tagline">America's best EF5 rated storm shelters and family safety products</p>
    <div class="brand-name">Steadfast</div>
    <div class="band"></div>
  </section>

  <section class="piece envelope-back" aria-label="Envelope back">
    <svg width="249" height="170" viewBox="0 0 249 170">
      <rect x="0.5" y="48.5" width="248" height="121" fill="#fff" stroke="#555"/>
      <polygon points="0,48 118,0 248,48 118,97" fill="#939598"/>
      <line x1="0" y1="48" x2="248" y2="48" stroke="#555"/>
    </svg>
    <div class="brand-name">Steadfast</div>
    <p class="address-line"><b>Address:</b> This is not actual address. This is only dummy text. Phone: XX 123456, XX 1234556, Fax: XX 123456</p>
  </section>

  <section class="piece folder-cover" aria-label="Presentation folder cover">
    <div class="brand-name"><span class="brand-mark"></span>Steadfast Shelters</div>
    <div class="band"></div>
    <p class="tagline">America's Best EF5 Rated Storm Shelters and Family Safety Products</p>
  </section>

  <section class="piece folder-back" aria-label="Presentation folder back">
    <div class="brand-name">Steadfast Shelters</div>
    <p class="address-line"><b>Address:</b> This is not actual address. This is only dummy text. Phone: XX 123456, XX 1234556, Fax: XX 123456</p>
    <p class="web-line">www.steadfast-example.com</p>
  </section>

  <section class="piece folder-inside-left" aria-label="Folder inside left panel"></section>

  <section class="piece folder-inside-right" aria-label="Folder inside pocket panel">
    <svg width="249" height="352" viewBox="0 0 249 352">
      <polygon points="8,307 78,268 249,268 249,352 8,352" fill="var(--brand-blue)"/>
    </svg>
  </section>
</main>
</body>
</html>
```